Website Design for Qolva-iX Software Solutions

Our company (IT) develops (3 main markets):
- Software for selfservice kiosks
- Web- and Mobile applications
- Embedded Software

```html
<!DOCTYPE html>
<html lang="nl">
<head>
<meta charset="utf-8">
<title>Qolva-iX Software Solutions – Web and Mobile applications</title>
<link rel="stylesheet" href="https://fonts.googleapis.com/css2?family=Arvo:wght@400;700&family=Arimo:wght@400;700&display=swap">
<style>
  :root {
    --blue-deep: #0a5f96;
    --blue-mid: #1479b8;
    --blue-light: #2a8fcc;
    --orange: #f7933f;
    --orange-dark: #e9742a;
    --green: #8cc63f;
    --green-light: #a6d65a;
    --green-text: #7ab32e;
    --title-blue: #3d7da6;
    --ink: #555555;
    --ink-soft: #777777;
    --page: #f1f1f1;
    --card: #ffffff;
    --footer-bar: #1d2a33;
  }
  * { margin: 0; padding: 0; box-sizing: border-box; }
  html, body { width: 867px; height: 1200px; overflow: hidden; }
  body {
    position: relative;
    background: var(--page);
    font-family: "Arimo", Arial, sans-serif;
    color: var(--ink);
  }
  .site-header {
    position: absolute; left: 0; top: 0; width: 867px; height: 262px;
    background: linear-gradient(180deg, var(--blue-mid) 0%, var(--blue-light) 45%, var(--blue-mid) 100%);
  }
  .brand {
    position: absolute; left: 123px; top: 32px;
    font-family: "Arvo", Georgia, serif; font-weight: 700;
    font-size: 33px; letter-spacing: 2px; color: #ffffff;
  }
  .main-nav {
    position: absolute; right: 121px; top: 40px;
    display: flex; align-items: center;
    font-family: "Arvo", Georgia, serif; font-weight: 700; font-size: 10px;
    letter-spacing: 0.6px;
  }
  .main-nav a { color: #0d4e7a; text-decoration: none; padding: 5px 9px; }
  .main-nav a.is-active {
    background: #0b4a72; color: #ffffff; border-radius: 8px;
    box-shadow: inset 0 1px 2px rgba(0,0,0,.4);
  }
  .main-nav a.is-active::after { content: " ▾"; font-size: 8px; }

  .intro {
    position: absolute; left: 120px; top: 119px; width: 626px; height: 300px;
    background: var(--card);
    box-shadow: 0 4px 10px rgba(0,0,0,.12);
  }
  .intro-banner {
    height: 111px;
    background: linear-gradient(180deg, #f9a257 0%, var(--orange) 60%, var(--orange-dark) 100%);
    border-bottom: 3px solid #d8641f;
    display: flex; align-items: center; padding-left: 32px;
  }
  .intro-banner svg { width: 36px; height: 62px; margin-right: 24px; }
  .intro-banner h1 {
    font-family: "Arvo", Georgia, serif; font-weight: 400; font-size: 27px; color: #ffffff;
    text-shadow: 0 1px 1px rgba(0,0,0,.15);
  }
  .intro-body { padding: 17px 19px 0 19px; }
  .intro-body h2 {
    font-family: "Arvo", Georgia, serif; font-weight: 400; font-size: 15.5px;
    color: var(--green-text); margin-bottom: 7px;
  }
  .intro-body p { font-size: 11px; line-height: 13.5px; color: #666; margin-bottom: 12px; }

  .projects-title {
    position: absolute; left: 120px; top: 447px;
    font-family: "Arvo", Georgia, serif; font-size: 17px; color: var(--green-text); font-weight: 400;
  }
  .project { position: absolute; top: 480px; width: 198px; text-align: center; }
  .project-shot {
    width: 198px; height: 109px; border: 3px solid #fff;
    box-shadow: 0 0 3px rgba(0,0,0,.3);
  }
  .project h3 {
    font-family: "Arvo", Georgia, serif; font-weight: 400; font-size: 12.5px;
    color: var(--title-blue); margin: 8px 0 5px;
  }
  .project p { font-size: 9.2px; line-height: 12px; color: var(--ink-soft); }

  .divider {
    position: absolute; left: 120px; top: 717px; width: 626px; height: 1px;
    background: linear-gradient(90deg, transparent, #d6d6d6, transparent);
  }
  .more-title {
    position: absolute; left: 0; width: 867px; top: 736px; text-align: center;
    font-family: "Arvo", Georgia, serif; font-size: 17px; color: var(--title-blue); font-weight: 400;
  }
  .showcase-button {
    position: absolute; left: 365px; top: 768px; width: 135px; height: 30px;
    background: linear-gradient(180deg, #b3dc78, var(--green));
    border: 1px solid #7aae35; border-radius: 4px;
    box-shadow: 0 2px 3px rgba(0,0,0,.2);
    display: flex; align-items: center; justify-content: center; gap: 7px;
    font-family: "Arvo", Georgia, serif; font-size: 11.5px; color: #3f5a1d; text-decoration: none;
  }

  .markets {
    position: absolute; left: 120px; top: 863px; width: 626px; height: 127px;
    display: flex; box-shadow: 0 6px 12px rgba(0,0,0,.18);
  }
  .market {
    flex: 1; display: flex; flex-direction: column; align-items: center; justify-content: flex-end;
    padding-bottom: 14px; color: #fff; font-family: "Arvo", Georgia, serif; font-size: 11.5px;
  }
  .market b { font-weight: 700; }
  .market svg { margin-bottom: 14px; }
  .market-web { background: linear-gradient(180deg, #f9a257, var(--orange-dark)); position: relative; flex: 0 0 208px; }
  .market-web::before {
    content: ""; position: absolute; top: -9px; left: 90px;
    border: 9px solid transparent; border-top: 0; border-bottom-color: #f9a257;
  }
  .market-kiosk, .market-embedded { background: linear-gradient(180deg, var(--green-light), #7cb835); }
  .markets-group { display: flex; flex: 1; border-top: 4px solid #9fd159; }

  .site-footer {
    position: absolute; left: 0; top: 1035px; width: 867px; height: 136px;
    background: linear-gradient(180deg, var(--blue-mid), var(--blue-deep));
  }
  .contact { position: absolute; left: 120px; top: 22px; font-family: "Arvo", Georgia, serif; }
  .contact h4, .about h4 { font-family: "Arvo", Georgia, serif; font-weight: 400; font-size: 14px; color: #fff; margin-bottom: 4px; }
  .contact p { font-size: 11.5px; color: #0e1f2b; line-height: 15px; padding-left: 2px; }
  .contact .hl { color: #b7e06a; }
  .contact .gap { margin-top: 13px; }
  .about { position: absolute; left: 334px; top: 22px; width: 412px; }
  .about p { font-size: 9.5px; line-height: 12px; color: #10283a; }
  .bottom-bar {
    position: absolute; left: 0; top: 1171px; width: 867px; height: 29px;
    background: linear-gradient(180deg, #2a3943, var(--footer-bar));
    font-family: "Arvo", Georgia, serif; font-size: 10px; color: #4f86ad;
    padding: 8px 0 0 119px;
  }
  .bottom-bar a { color: #2f78a8; text-decoration: none; margin-left: 6px; }
</style>
</head>
<body>
  <header class="site-header">
    <div class="brand">QOLVA-IX</div>
    <nav class="main-nav">
      <a href="#">HOME</a>
      <a href="#">NEWS</a>
      <a href="#">SHOWCASE</a>
      <a href="#" class="is-active">SERVICES</a>
      <a href="#">CONTACT</a>
    </nav>
  </header>

  <section class="intro">
    <div class="intro-banner">
      <svg viewBox="0 0 36 62" aria-hidden="true">
        <rect x="2" y="2" width="32" height="58" rx="5" fill="#fff" opacity=".95"/>
        <rect x="5" y="9" width="26" height="40" fill="#f7933f"/>
        <circle cx="18" cy="54.5" r="2.6" fill="#f7933f"/>
      </svg>
      <h1>Web and Mobile applications</h1>
    </div>
    <div class="intro-body">
      <h2>We have the tools to create universal, usable, and beautiful applications.</h2>
      <p>Voor diverse klanten hebben we applicaties naar de browser toe gebracht. Dat betekent dat onze klanten vanaf iedere gewenste locatie bij hun gegevens kunnen en deze kunnen verrijken. We zien steeds meer overlap van webapplicaties naar mobiele apparaten als telefoons en tablets. Webapplicaties kunnen prima functioneren op een telefoon of tablet, maar in sommige gevallen is het wenselijker een applicatie te schrijven voor op de telefoon of tablet zelf, waarbij de data vanuit een centraal datacenter komt.</p>
      <p>Qolva-iX biedt haar klanten kennis en ervaring op beide vakgebieden. Zo is er ervaring met een groot aantal mobiele platformen (denk aan: Orbit OS, KeyBerry, Droidline, Symphos, Wintab Mobile) en ontwikkelen we ook applicaties voor tablets met een volledig Wintab besturingssysteem.</p>
    </div>
  </section>

  <h2 class="projects-title">Latest Web/Mobile Projects</h2>

  <article class="project" style="left:119px">
    <div class="project-shot" role="img" aria-label="Screenshot of the Train Like a Winner website" style="background:linear-gradient(180deg,#e9833a 0%,#f2f2f2 22%,#2b2b2b 40%,#1a1a1a 100%)"></div>
    <h3>Train Like a Winner</h3>
    <p>Write a short description of the project in question here. Mauris cursus mauris eu turpis gravida scelerisque. Quisque lectus nulla, pellentesque id pretium vel, posuere eu purus. Integer a lacus at nibh ultricies facilisis.</p>
  </article>
  <article class="project" style="left:333px">
    <div class="project-shot" role="img" aria-label="Screenshot of the Le Stade Sport Quiz website" style="background:linear-gradient(180deg,#d0202a 0%,#c41820 26%,#eaeaea 34%,#7a4a22 50%,#4a2a14 100%)"></div>
    <h3>Le Stade Sport Quiz</h3>
    <p>Etiam ultrices dui in tellus aliquet feugiat blandit augue lobortis. Lorem ipsum dolor sit amet, consectetur adipiscing elit.Quisque lectus nulla, pellentesque id pretium vel, posuere eu purus. Integer a lacus at nibh ultricies facilisis.</p>
  </article>
  <article class="project" style="left:547px">
    <div class="project-shot" role="img" aria-label="Screenshot of the Doelpuntquiz website" style="background:linear-gradient(180deg,#d41a22 0%,#b8121a 36%,#2e3a48 44%,#1f5a22 62%,#2d7a2a 100%)"></div>
    <h3>Doelpuntquiz</h3>
    <p>Lorem ipsum dolor sit amet, consectetur adipiscing elit. Mauris cursus mauris eu turpis gravida scelerisque. Quisque lectus nulla, pellentesque id pretium vel, posuere eu purus. Integer a lacus at nibh ultricies facilisis. Etiam ultrices dui in.</p>
  </article>

  <div class="divider"></div>
  <h2 class="more-title">Want to see more projects?</h2>
  <a class="showcase-button" href="#">
    <svg width="12" height="10" viewBox="0 0 12 10" aria-hidden="true"><rect x=".5" y=".5" width="11" height="9" fill="none" stroke="#3f5a1d"/><path d="M2 8 L5 4 L7 6 L8.5 4.5 L10 8 Z" fill="#3f5a1d"/></svg>
    View the showcase
  </a>

  <section class="markets">
    <div class="market market-web">
      <svg width="36" height="62" viewBox="0 0 36 62" aria-hidden="true">
        <rect x="2" y="2" width="32" height="58" rx="5" fill="#fff"/>
        <rect x="5" y="9" width="26" height="40" fill="#f7933f"/>
        <circle cx="18" cy="54.5" r="2.6" fill="#f7933f"/>
      </svg>
      <span><b>Web / Mobile</b> applications</span>
    </div>
    <div class="markets-group">
      <div class="market market-kiosk">
        <svg width="54" height="60" viewBox="0 0 54 60" aria-hidden="true">
          <rect x="2" y="2" width="50" height="36" rx="3" fill="#fff"/>
          <rect x="7" y="7" width="40" height="26" fill="#94cc4a"/>
          <rect x="21" y="38" width="12" height="14" fill="#fff"/>
          <rect x="10" y="52" width="34" height="6" rx="2" fill="#fff"/>
        </svg>
        <span><b>Self-service</b> kiosk software</span>
      </div>
      <div class="market market-embedded">
        <svg width="68" height="60" viewBox="0 0 68 60" aria-hidden="true">
          <g fill="none" stroke="#fff" stroke-width="5">
            <circle cx="9" cy="50" r="6"/>
            <circle cx="32" cy="33" r="6"/>
            <circle cx="57" cy="12" r="7"/>
            <path d="M13 45 L20 38 H27 M37 30 L44 23 L51 17"/>
          </g>
        </svg>
        <span><b>Embedded</b> Software</span>
      </div>
    </div>
  </section>

  <footer class="site-footer">
    <div class="contact">
      <h4>Get in touch with us</h4>
      <p>Call us: <span class="hl">555-0148-2290</span></p>
      <p>Email: <span class="hl">hello@example.com</span></p>
      <p class="gap">Or use our <span class="hl">contact form</span>.</p>
    </div>
    <div class="about">
      <h4>About Us</h4>
      <p>We are an <b>independent software company</b>. Lorem ipsum dolor sit amet, consectetur adipiscing elit. In nibh ipsum, imperdiet vel elementum nec, vulputate et erat. Aliquam vel leo lacinia neque ornare cursus. Vestibulum dui purus, feugiat ac pulvinar sit amet, vulputate a eros. Sed metus metus, commodo sollicitudin fringilla et, accumsan nec metus. Suspendisse eu purus risus, id dignissim magna. Integer facilisis ante quis mi condimentum ut congue diam fermentum.</p>
    </div>
  </footer>
  <div class="bottom-bar">Copyright © 2012 Qolva-iX.&nbsp; All rights reserved. <a href="#">Terms and Privacy Policy</a></div>
</body>
</html>
```